Dutch psychology podcast needs logo / art design

I need a logo / artwork for my new podcast on psychology/health called 'Het Heldere Kwartier'. In the podcast I talk to different experts on subjects as personal development, psychology, health, spirituality and entrepreneurship. I would like to see my brand colors back in the design (www.joramveldkuijl.nl) and my face in the artwork since I'm the host of the show.

My photo is included in the attachments and I've also added some examples of what I'm looking for.

Industry/Entity Type

Psychology

Colors

Designer to choose colors to be used in the design.

Requirements
Must have
• - Name of the show: 'Het Heldere Kwartier' (I prefer that this name is turned into a logo), see attachment of example of Harbor of Wonder
• - Subtitle: 'met Joram Veldkuijl' which is my name a the host
• - My picture, see attachments

```html
<!DOCTYPE html>
<html lang="nl">
<head>
<meta charset="utf-8">
<title>Het Heldere Kwartier – podcast artwork</title>
<link rel="stylesheet" href="https://fonts.googleapis.com/css2?family=Oswald:wght@300;500&family=Open+Sans:wght@700;800&family=Montserrat:wght@300;700&display=swap">
<style>
  :root {
    --teal-deep: #05473f;
    --teal-mid: #0f8a76;
    --teal-bright: #1fc7ad;
    --cyan-glow: #2af3e6;
    --topic-ink: rgba(4, 60, 52, 0.55);
    --title-white: #ffffff;
    --host-placeholder-top: #1b3a4a;
    --host-placeholder-bottom: #0c1420;
  }
  * { margin: 0; padding: 0; box-sizing: border-box; }
  html, body { width: 1200px; height: 1200px; overflow: hidden; background: var(--teal-deep); }

  .cover {
    position: relative;
    width: 1200px;
    height: 1200px;
    overflow: hidden;
    background:
      radial-gradient(ellipse 520px 620px at 180px 520px, rgba(42, 243, 230, 0.85), rgba(42, 243, 230, 0) 70%),
      radial-gradient(ellipse 700px 700px at 700px 450px, var(--teal-bright), rgba(31, 199, 173, 0) 75%),
      linear-gradient(135deg, var(--teal-mid) 0%, #0c7564 55%, var(--teal-deep) 100%);
  }

  .diagonal-bands { position: absolute; inset: 0; width: 1200px; height: 1200px; }

  .topic {
    position: absolute;
    font-family: "Open Sans", sans-serif;
    font-weight: 700;
    color: var(--topic-ink);
    white-space: nowrap;
    line-height: 1;
  }
  .topic--health { left: 52px; top: 38px; font-size: 74px; font-weight: 800; }
  .topic--psychology { left: 489px; top: 142px; font-size: 56px; }
  .topic--development { left: 660px; top: 608px; font-size: 33px; }
  .topic--entrepreneurship { left: 714px; top: 760px; font-size: 48px; }
  .topic--spirituality { left: 762px; top: 928px; font-size: 68px; font-weight: 800; }

  .host-photo {
    position: absolute;
    left: 0;
    top: 62px;
    width: 800px;
    height: 1138px;
    border-radius: 140px 140px 0 0 / 160px 160px 0 0;
    background: linear-gradient(180deg, var(--host-placeholder-top) 0%, var(--host-placeholder-bottom) 70%);
    clip-path: polygon(26% 0, 63% 0, 63% 44%, 84% 50%, 99% 100%, 0 100%, 0 52%, 26% 45%);
  }

  .show-title {
    position: absolute;
    left: 556px;
    top: 0;
    width: 600px;
    height: 600px;
    font-family: "Oswald", sans-serif;
    color: var(--title-white);
    text-transform: uppercase;
    line-height: 1;
    font-weight: 500;
  }
  .show-title__line {
    position: absolute;
    left: 0;
    width: 600px;
    text-align: center;
    white-space: nowrap;
  }
  .show-title__line--het { top: 57px; font-size: 172px; font-weight: 500; }
  .show-title__line--heldere { top: 227px; font-size: 172px; font-weight: 300; }
  .show-title__line--kwartier { top: 414px; font-size: 140px; font-weight: 500; }

  .host-name {
    position: absolute;
    left: 560px;
    top: 1074px;
    width: 600px;
    text-align: center;
    font-family: "Montserrat", sans-serif;
    font-size: 56px;
    color: var(--title-white);
    white-space: nowrap;
    line-height: 1;
  }
  .host-name__first { font-weight: 700; }
  .host-name__last { font-weight: 300; }
</style>
</head>
<body>
  <main class="cover">
    <svg class="diagonal-bands" viewBox="0 0 1200 1200" aria-hidden="true">
      <polygon points="0,760 700,60 820,60 0,880" fill="rgba(255,255,255,0.07)"/>
      <polygon points="0,1000 920,80 1000,80 0,1080" fill="rgba(255,255,255,0.05)"/>
      <polygon points="500,1200 1200,500 1200,640 640,1200" fill="rgba(0,40,35,0.18)"/>
      <polygon points="820,1200 1200,820 1200,900 900,1200" fill="rgba(255,255,255,0.05)"/>
    </svg>

    <span class="topic topic--health">health</span>
    <span class="topic topic--psychology">psychology</span>
    <span class="topic topic--development">personal development</span>
    <span class="topic topic--entrepreneurship">entrepreneurship</span>
    <span class="topic topic--spirituality">spirituality</span>

    <div class="host-photo" role="img" aria-label="Portretfoto van host Joram Veldkuijl, lachend met gekruiste armen in een donkere trui"></div>

    <h1 class="show-title">
      <span class="show-title__line show-title__line--het">Het</span>
      <span class="show-title__line show-title__line--heldere">Heldere</span>
      <span class="show-title__line show-title__line--kwartier">Kwartier</span>
    </h1>

    <p class="host-name"><span class="host-name__first">JORAM</span><span class="host-name__last">VELDKUIJL</span></p>
  </main>
</body>
</html>
```